Briefing for Nexoria Desk Business Card Design:

Objective:
To design business cards that represent the vision and mission of Nexoria Desk, a company that aims to create the best remote work experience for people and companies, with a focus on simplicity and ease of use.

Design Elements:

Color Scheme: Blue and White
Font: Modern and Clean
Logo: The Nexoria Desk logo should be prominently displayed on the card.
Vision Statement: "Helping businesses create workplaces where people love to work" should be included on the card.
Mission Statement: "Create the best remote work experience for people and companies" should also be included.
Key Focus: The card should emphasize Nexoria Desk's focus on simplicity and ease of use in its cloud solutions.
Design Concept:
The design of the business card should be simple yet professional. The Nexoria Desk logo should be the focal point of the card, and the blue and white color scheme should be used to create a clean and modern feel that reinforces the idea of simplicity and ease of use. Blue represents trust, professionalism, and reliability, while white represents purity, simplicity, and clarity. The card should feature the vision and mission of the company, with each statement being given equal importance. The font used should be modern and clean, with legibility being a top priority. A tagline could be included that emphasizes the company's focus on simplicity and ease of use, such as "Simplicity at its best" or "Streamlined cloud solutions."

Final Thoughts:
The design of the business card should represent Nexoria Desk's vision and mission while also conveying the message that the company is the choice for those who value simplicity and ease of use in their cloud solutions. The final product should leave a lasting impression on anyone who receives it, and it should convey the professionalism and expertise of Nexoria Desk in helping businesses create workplaces where people love to work. The blue and white color scheme can be a great choice for the Nexoria Desk business card design, and it can help to create a professional and memorable impression on clients and partners while emphasizing the company's focus on simplicity and ease of use.

Target Market(s)

Companies that employ remote workers that work on computers

Industry/Entity Type

SaaS

Contact Information for Business Card

Website: www.nexoriadesk.example, phone, email, whatsApp, LinkedIn,

Font styles to use
Other font styles liked:
• Main Fonts: Poppins Light, Poppins Medium, Poppins Bold Alternative Fonts (for Sub Headers) Cairo Light, Cairo Regular, Cairo Bold

Colors
0054AA
0677BA
7BADD7
CADEEF
E8F1F8

Requirements
Must have
Nice to have
• Most of of our competitors treat you like a number, we give a sh!t, we take the time to help people get set up and grow. Think of the Zorvan vs Plinthar commercials from the early 2000s

```html
<!DOCTYPE html>
<html lang="en">
<head>
<meta charset="utf-8">
<title>Nexoria Desk – Business Card Concepts</title>
<link rel="stylesheet" href="https://fonts.googleapis.com/css2?family=Barlow:wght@400&family=Poppins:wght@400;500;600;700&display=swap">
<style>
  :root {
    --blue: #1475e6;
    --ink-blue: #1a6fd6;
    --navy: #0d4a82;
    --mark: #1c7bc4;
    --white: #ffffff;
    --sheet: #ffffff;
    --backdrop: #dcdcdc;
    --shadow: rgba(0, 0, 0, 0.22);
  }
  * { margin: 0; padding: 0; box-sizing: border-box; }
  html, body { width: 1200px; height: 771px; overflow: hidden; background: var(--sheet); }
  body { position: relative; font-family: "Poppins", sans-serif; color: var(--ink-blue); }

  .card {
    position: absolute; width: 524px; height: 339px; overflow: hidden;
    background: var(--white); box-shadow: 0 6px 16px var(--shadow);
  }
  .card--split   { left: 57px;  top: 38px; }
  .card--pill    { left: 617px; top: 38px; }
  .card--banded  { left: 57px;  top: 392px; }
  .backdrop      { position: absolute; left: 617px; top: 392px; width: 524px; height: 339px;
                   background: var(--backdrop); box-shadow: 0 6px 16px var(--shadow); }

  .abs { position: absolute; }
  .center { text-align: center; }
  .statement { font-family: "Barlow", sans-serif; font-size: 17px; line-height: 21px; font-weight: 400; white-space: nowrap; }
  .on-blue { color: var(--white); }

  .brand { position: absolute; display: flex; flex-direction: column; align-items: center; }
  .brand-mark { border-radius: 50%; background: var(--mark); }
  .brand-name { font-weight: 700; color: var(--navy); white-space: nowrap; letter-spacing: -0.5px; }

  .address { font-size: 17px; line-height: 21px; white-space: nowrap; }
  .address .phone { font-size: 18px; line-height: 26px; }
  .address .web { font-size: 13px; line-height: 18px; }

  .contact { position: absolute; display: flex; align-items: center; gap: 7px; font-size: 12px; white-space: nowrap; }
  .contact--mail { font-size: 11px; }
  .icon { width: 17px; height: 17px; flex: none; }
  .icon-square { width: 15px; height: 15px; flex: none; background: currentColor; border-radius: 2px; }

  .split-panel { left: 191px; top: 42px; width: 333px; height: 216px; background: var(--blue);
                 border-radius: 20px 0 0 20px; }

  .pill { left: 0; top: 65px; width: 524px; height: 210px; background: var(--blue); border-radius: 105px; }
  .pill .contact { color: var(--white); }

  .band { left: 0; width: 524px; background: var(--blue); }
</style>
</head>
<body>

<section class="card card--split">
  <div class="brand" style="left:2px; top:48px; width:200px;">
    <div class="brand-mark" style="width:90px; height:90px; margin-bottom:18px;"></div>
    <div class="brand-name" style="font-size:25px;">Nexoria Desk</div>
  </div>
  <div class="abs center address" style="left:0; top:232px; width:194px;">
    <div>Northvale, Canada</div>
    <div>Harbor Point, USA</div>
    <div class="phone">1-555-010-4477</div>
    <div class="web" style="font-size:12px;">www.nexoriadesk.example</div>
  </div>

  <div class="abs split-panel">
    <div class="abs center statement on-blue" style="left:0; top:22px; width:333px;">
      <div>Vision :</div>
      <div>"Helping businesses create<br>workplaces where people love to work"</div>
    </div>
    <div class="abs center statement on-blue" style="left:0; top:119px; width:333px;">
      <div>Mission :</div>
      <div>"Create the best remote work experience<br>for people and companies"</div>
    </div>
  </div>

  <div class="contact" style="left:197px; top:275px;">
    <svg class="icon" viewBox="0 0 24 24"><path fill="currentColor" d="M6.6 10.8a15 15 0 0 0 6.6 6.6l2.2-2.2c.3-.3.7-.4 1-.2 1.1.4 2.3.6 3.6.6.6 0 1 .4 1 1V20c0 .6-.4 1-1 1A17 17 0 0 1 3 4c0-.6.4-1 1-1h3.5c.6 0 1 .4 1 1 0 1.3.2 2.5.6 3.6.1.3 0 .7-.2 1z"/></svg>
    <span>1-555-010-4477</span>
  </div>
  <div class="contact" style="left:198px; top:297px;">
    <span class="icon-square"></span><span style="margin-left:6px;">nexoriadesk</span>
  </div>
  <div class="contact contact--mail" style="left:330px; top:274px;">
    <svg class="icon" viewBox="0 0 24 24"><rect x="2" y="5" width="20" height="14" fill="none" stroke="currentColor" stroke-width="1.6"/><path d="M2 5l10 8 10-8M2 19l7-7M22 19l-7-7" fill="none" stroke="currentColor" stroke-width="1.4"/></svg>
    <span>hello@nexoriadesk.example</span>
  </div>
  <div class="contact contact--mail" style="left:331px; top:296px;">
    <span class="icon-square"></span><span>nexoria-desk-solutions</span>
  </div>
</section>

<section class="card card--pill">
  <div class="abs center statement" style="left:0; top:17px; width:524px;">
    <div>Vision :</div>
    <div>"Helping businesses create workplaces where people love to work"</div>
  </div>

  <div class="abs pill">
    <div class="abs center address on-blue" style="left:10px; top:54px; width:190px;">
      <div>Northvale, Canada</div>
      <div>Harbor Point, USA</div>
      <div class="phone" style="line-height:30px;">1-555-010-4477</div>
      <div style="font-size:12.5px; line-height:22px;">www.nexoriadesk.example</div>
    </div>
    <div class="brand" style="left:192px; top:26px; width:130px;">
      <div class="brand-mark" style="width:100px; height:100px; margin-bottom:14px; border:4px solid var(--white);"></div>
      <div class="brand-name" style="font-size:21px; color:var(--white);">Nexoria Desk</div>
    </div>
    <div class="contact" style="left:322px; top:58px; font-size:14px;">
      <svg class="icon" viewBox="0 0 24 24"><path fill="currentColor" d="M6.6 10.8a15 15 0 0 0 6.6 6.6l2.2-2.2c.3-.3.7-.4 1-.2 1.1.4 2.3.6 3.6.6.6 0 1 .4 1 1V20c0 .6-.4 1-1 1A17 17 0 0 1 3 4c0-.6.4-1 1-1h3.5c.6 0 1 .4 1 1 0 1.3.2 2.5.6 3.6.1.3 0 .7-.2 1z"/></svg>
      <span>1-555-010-4477</span>
    </div>
    <div class="contact contact--mail" style="left:322px; top:84px;">
      <svg class="icon" viewBox="0 0 24 24"><rect x="2" y="5" width="20" height="14" fill="none" stroke="currentColor" stroke-width="1.6"/><path d="M2 5l10 8 10-8M2 19l7-7M22 19l-7-7" fill="none" stroke="currentColor" stroke-width="1.4"/></svg>
      <span>hello@nexoriadesk.example</span>
    </div>
    <div class="contact" style="left:323px; top:110px; font-size:13px;">
      <span class="icon-square"></span><span style="margin-left:8px;">nexoriadesk</span>
    </div>
    <div class="contact" style="left:323px; top:135px;">
      <span class="icon-square"></span><span>nexoria-desk-solutions</span>
    </div>
  </div>

  <div class="abs center statement" style="left:0; top:279px; width:524px;">
    <div>Mission :</div>
    <div>"Create the best remote work experience for people and companies"</div>
  </div>
</section>

<section class="card card--banded">
  <div class="abs band" style="top:0; height:64px;">
    <div class="abs center statement on-blue" style="left:0; top:12px; width:524px;">
      <div>Vision :</div>
      <div>"Helping businesses create workplaces where people love to work"</div>
    </div>
  </div>

  <div class="brand" style="left:4px; top:82px; width:200px;">
    <div class="brand-mark" style="width:100px; height:100px; margin-bottom:38px;"></div>
    <div class="brand-name" style="font-size:27px;">Nexoria Desk</div>
  </div>

  <div class="abs center" style="left:225px; top:96px; width:250px; font-size:18px; line-height:24px; white-space:nowrap;">
    <div>Northvale, Canada</div>
    <div>Harbor Point, USA</div>
    <div style="line-height:27px;">1-555-010-4477</div>
    <div style="font-size:16px;">www.nexoriadesk.example</div>
  </div>

  <div class="contact" style="left:205px; top:220px;">
    <svg class="icon" viewBox="0 0 24 24"><path fill="currentColor" d="M6.6 10.8a15 15 0 0 0 6.6 6.6l2.2-2.2c.3-.3.7-.4 1-.2 1.1.4 2.3.6 3.6.6.6 0 1 .4 1 1V20c0 .6-.4 1-1 1A17 17 0 0 1 3 4c0-.6.4-1 1-1h3.5c.6 0 1 .4 1 1 0 1.3.2 2.5.6 3.6.1.3 0 .7-.2 1z"/></svg>
    <span>1-555-010-4477</span>
  </div>
  <div class="contact" style="left:206px; top:242px;">
    <span class="icon-square"></span><span style="margin-left:6px;">nexoriadesk</span>
  </div>
  <div class="contact contact--mail" style="left:335px; top:219px;">
    <svg class="icon" viewBox="0 0 24 24"><rect x="2" y="5" width="20" height="14" fill="none" stroke="currentColor" stroke-width="1.6"/><path d="M2 5l10 8 10-8M2 19l7-7M22 19l-7-7" fill="none" stroke="currentColor" stroke-width="1.4"/></svg>
    <span>hello@nexoriadesk.example</span>
  </div>
  <div class="contact contact--mail" style="left:336px; top:241px;">
    <span class="icon-square"></span><span>nexoria-desk-solutions</span>
  </div>

  <div class="abs band" style="top:273px; height:66px;">
    <div class="abs center statement on-blue" style="left:0; top:10px; width:524px;">
      <div>Mission :</div>
      <div>"Create the best remote work experience for people and companies"</div>
    </div>
  </div>
</section>

<div class="backdrop"></div>

</body>
</html>
```